Hedge Fund Business Presentation for prospective clients

We need a professional design for our PowerPoint presentation that we use to send to prospective clients for our Alternative Investments/Hedge Fund. This presentation needs to have the same verbiage as what is being used already. We will present this to individuals, institutions (banks, non profits), and to Registered Investment Advisors that have client money to place.

Target Market(s)

High net worth individuals, high income earners, doctors, lawyers, business owners, sophisticated investors

Industry/Entity Type

Investment Advisory

Font styles to use
Other font styles liked:
• font that is in logo

Requirements
Must have
• a very simple, but professional, elegant design. must include our color scheme, feel free to add other shades in our scheme.

```html
<!DOCTYPE html>
<html lang="en">
<head>
<meta charset="utf-8">
<title>Bastion Meridian — Investor Presentation Slides</title>
<link rel="stylesheet" href="https://fonts.googleapis.com/css2?family=Tinos:ital,wght@0,400;0,700;1,400&family=Arimo:wght@400;700&family=Montserrat:wght@700;800&display=swap">
<style>
:root{
  --teal-deep:#0d3340;
  --teal-accent:#5fa3b5;
  --navy-slate:#1f3a4c;
  --slate-card:#2c3b4f;
  --brand-blue:#1a5fa8;
  --bright-blue:#1b76c9;
  --paper:#f1f2f4;
  --white:#fff;
}
*{box-sizing:border-box;margin:0;padding:0}
html,body{width:1200px;height:1200px;overflow:hidden;background:#fff}
.board{position:absolute;left:0;top:0;width:1500px;height:1500px;transform:scale(.8);transform-origin:0 0}
.slide{position:absolute;overflow:hidden}
.abs{position:absolute}
.serif{font-family:"Tinos","Times New Roman",serif}
.wordmark{font-family:"Tinos","Times New Roman",serif;font-weight:400;white-space:nowrap;letter-spacing:1px}
.subline{font-family:"Tinos","Times New Roman",serif;font-style:italic;white-space:nowrap}
.center{text-align:center}
.page-num{position:absolute;width:14px;height:14px;border-radius:50%;font:8px "Arimo",sans-serif;display:flex;align-items:center;justify-content:center}

/* Contact cover */
.accent-teal{position:absolute;left:536px;top:102px;width:214px;height:406px;background:var(--teal-accent)}
.contact-cover{left:37px;top:112px;width:703px;height:386px;background:linear-gradient(160deg,#12404d 0%,var(--teal-deep) 55%,#0a2a35 100%)}
.contact-cover .person{color:var(--white);font-size:15px;line-height:18px;width:260px;margin-left:-130px}
.contact-cover .footer-bar{left:0;top:335px;width:100%;height:51px;background:#050505;color:#fff;font-size:13px;display:flex;align-items:center;justify-content:center}

/* Title slide */
.title-slide{left:780px;top:102px;width:713px;height:400px;background:linear-gradient(180deg,#a9cbe6 0%,#e3eef7 45%,#6e9fc8 75%,#1e5d98 100%)}
.title-slide .tower{right:0;top:0;width:300px;height:100%;background:linear-gradient(100deg,rgba(40,90,150,0) 0%,rgba(40,90,150,.55) 40%,rgba(20,60,110,.8) 100%)}
.title-slide .band{left:0;top:116px;width:100%;height:176px;background:rgba(255,255,255,.72)}
.title-slide .dark-band{left:0;top:292px;width:100%;height:27px;background:#2a3a4c;color:#fff;font-size:15px;display:flex;align-items:center;justify-content:center}

/* Managing members */
.members{left:26px;top:532px;width:711px;height:399px;background:linear-gradient(170deg,#b9cddd 0%,#8fbbe0 40%,#4f9fe0 75%,#3d92dc 100%)}
.members .head-tab{left:349px;top:40px;width:362px;height:71px;background:#050505;clip-path:polygon(70px 0,100% 0,100% 100%,0 100%)}
.members .head-tab h2{position:absolute;left:83px;top:14px;font:700 25px "Tinos",serif;color:#fff;letter-spacing:.5px}
.members .head-tab .rule{position:absolute;left:45px;top:51px;width:300px;height:5px;background:var(--bright-blue)}
.name-card{position:absolute;background:#fff;box-shadow:0 2px 4px rgba(0,0,0,.25);width:258px;height:85px}
.name-card .portrait{position:absolute;left:8px;top:4px;width:78px;height:77px;background:linear-gradient(135deg,#d9d9d9,#8a8a8a)}
.name-card .nm{position:absolute;left:104px;top:18px;font:700 20px/25px "Tinos",serif;color:#111;letter-spacing:.5px}
.info-tag{position:absolute;background:#fff;width:170px;height:62px;box-shadow:0 2px 4px rgba(0,0,0,.25);padding:14px 0 0 12px;font:9.5px/12.5px "Tinos",serif;color:#111}
.connector{position:absolute;background:var(--brand-blue)}
.dot{position:absolute;width:8px;height:8px;border-radius:50%;background:var(--brand-blue)}
.members .firm{left:64px;top:278px;color:#1b2a38;font:13px/16px "Tinos",serif}

/* Overview */
.overview{left:790px;top:550px;width:698px;height:380px;background:var(--paper)}
.overview h2{position:absolute;left:30px;top:36px;font:800 23px "Montserrat",sans-serif;color:var(--bright-blue);letter-spacing:-.5px}
.overview .rule{left:32px;top:66px;width:202px;height:3px;background:#111}
.ov-box{position:absolute;top:96px;width:180px;height:227px;border-radius:0 26px 0 0;color:#fff;box-shadow:0 8px 6px -4px rgba(0,0,0,.35)}
.ov-box.blue{background:linear-gradient(180deg,#1d6fc0 0%,#0d3f86 100%)}
.ov-box.dark{background:var(--slate-card)}
.ov-box h3{position:absolute;font:400 15px/17px "Tinos",serif;letter-spacing:.5px}
.ov-box p{position:absolute;font:11px/14px "Arimo",sans-serif}
.arrow{position:absolute;top:212px;width:36px;height:16px}

/* Why slides */
.accent-blue{position:absolute;background:var(--bright-blue)}
.why{background:linear-gradient(160deg,#1e3c50 0%,var(--navy-slate) 50%,#17323f 100%)}
.why h2{position:absolute;font:800 21px "Montserrat",sans-serif;color:#fff;letter-spacing:-.5px;white-space:nowrap}
.why .title-rule{position:absolute;height:4px;background:var(--bright-blue)}
.why .feat-head{position:absolute;font:14px "Tinos",serif;color:#fff;white-space:nowrap}
.why .feat-text{position:absolute;font:10.5px/13px "Arimo",sans-serif;color:#fff;width:180px}
.why .feat-text.serif-small{font:10px/11px "Tinos",serif}
.why .divider{position:absolute;width:1px;background:rgba(255,255,255,.2)}
.why .body{position:absolute;color:#fff;font:13.5px/16px "Arimo",sans-serif}
.why ul{list-style:none}
.why li{position:relative;padding-left:17px}
.why li::before{content:"•";position:absolute;left:0}
.icon{position:absolute}
</style>
</head>
<body>
<div class="board">

  <!-- Contact cover -->
  <div class="accent-teal"></div>
  <section class="slide contact-cover" role="img" aria-label="Dark teal backdrop of looking up at office towers">
    <div class="abs wordmark center" style="left:0;width:100%;top:56px;font-size:30px;color:#fff">BASTION MERIDIAN LLC</div>
    <div class="abs subline center" style="left:0;width:100%;top:100px;font-size:13px;color:#fff">Measured Capital Stewardship</div>
    <div class="abs person serif center" style="left:230px;top:158px">Walter B. Hensley<br>Managing Member<br>Phone: 555.210.4417<br>Walt@BastionMeridian.com</div>
    <div class="abs person serif center" style="left:460px;top:158px">Daniel R. Pryce<br>Managing Member<br>Office: 555.362.9180<br>Daniel@BastionMeridian.com</div>
    <div class="abs serif center" style="left:0;width:100%;top:289px;font-size:8px;color:#fff">48 Oakridge Lane &nbsp;|&nbsp; Fairhill, AL 35000 &nbsp;|&nbsp; Office: 555.210.4417 &nbsp;|&nbsp; BastionMeridian.com</div>
    <div class="abs footer-bar serif">Patience in Research. Discipline in Practice.</div>
  </section>

  <!-- Title slide -->
  <section class="slide title-slide">
    <div class="abs tower" role="img" aria-label="Glass office tower reflecting a blue sky"></div>
    <div class="abs band"></div>
    <svg class="abs" style="left:0;top:0" width="713" height="400" aria-hidden="true">
      <line x1="0" y1="120" x2="120" y2="0" stroke="#fff" stroke-opacity=".6" stroke-width="2"/>
      <line x1="560" y1="400" x2="713" y2="230" stroke="#fff" stroke-opacity=".5" stroke-width="2"/>
      <polygon points="600,400 713,290 713,400" fill="#1b5fa6" opacity=".6"/>
    </svg>
    <div class="abs wordmark center" style="left:0;width:100%;top:156px;font-size:50px;color:var(--brand-blue)">BASTION MERIDIAN LLC</div>
    <div class="abs subline center" style="left:0;width:100%;top:226px;font-size:20px;color:#1b2230">Measured Capital Stewardship</div>
    <div class="abs dark-band serif">Patience in Research. Discipline in Practice.</div>
    <div class="abs wordmark" style="left:45px;top:362px;font-size:13px;color:#fff">BASTION MERIDIAN LLC</div>
  </section>

  <!-- Managing members -->
  <section class="slide members" role="img" aria-label="Blue-toned photo of a business meeting with a tablet">
    <div class="abs" style="left:0;top:0;width:100%;height:12px;background:rgba(255,255,255,.35)"></div>
    <div class="abs head-tab"><h2>Managing Members</h2><div class="rule"></div></div>

    <div class="connector" style="left:71px;top:135px;width:2px;height:46px"></div>
    <div class="connector" style="left:71px;top:179px;width:22px;height:2px"></div>
    <div class="dot" style="left:68px;top:131px"></div>
    <div class="name-card" style="left:54px;top:51px"><div class="portrait" role="img" aria-label="Portrait of Walter B. Hensley"></div><div class="nm">WALTER B.<br>HENSLEY</div></div>
    <div class="info-tag" style="left:92px;top:146px">Co-Founder &amp; Managing Member<br>Phone: 555.210.4417<br>Walt@BastionMeridian.com</div>

    <div class="connector" style="left:364px;top:222px;width:2px;height:46px"></div>
    <div class="connector" style="left:364px;top:266px;width:22px;height:2px"></div>
    <div class="dot" style="left:361px;top:218px"></div>
    <div class="name-card" style="left:346px;top:137px"><div class="portrait" role="img" aria-label="Portrait of Daniel R. Pryce"></div><div class="nm">DANIEL R.<br>PRYCE</div></div>
    <div class="info-tag" style="left:384px;top:232px">Co-Founder &amp; Managing Member<br>Phone: 555.362.9180<br>Daniel@BastionMeridian.com</div>

    <div class="abs firm">Bastion Meridian, LLC<br>48 Oakridge Lane &nbsp;|&nbsp; Fairhill AL 35000<br>Office: 555.210.4417<br>BastionMeridian.com</div>
    <div class="abs wordmark" style="left:496px;top:318px;font-size:13px;color:#fff">BASTION MERIDIAN LLC</div>
    <div class="abs" style="left:64px;top:353px;width:602px;height:2px;background:#2b3f55"></div>
    <div class="page-num" style="left:675px;top:364px;background:#111;color:#fff">2</div>
  </section>

  <!-- Overview -->
  <section class="slide overview">
    <h2>OVERVIEW</h2>
    <div class="abs rule"></div>
    <div class="abs wordmark" style="left:545px;top:30px;font-size:10px;color:var(--brand-blue);letter-spacing:.5px">BASTION MERIDIAN LLC</div>

    <div class="ov-box blue" style="left:30px">
      <svg class="icon" style="left:14px;top:30px" width="30" height="30" viewBox="0 0 30 30" aria-hidden="true"><circle cx="15" cy="15" r="14" fill="none" stroke="#fff" stroke-width="2"/><circle cx="15" cy="11" r="4" fill="#fff"/><path d="M7 22c1-5 15-5 16 0z" fill="#fff"/><circle cx="9" cy="12" r="2.5" fill="#fff"/><circle cx="21" cy="12" r="2.5" fill="#fff"/></svg>
      <h3 style="left:51px;top:30px">MANAGEMENT<br>TEAM</h3>
      <p style="left:13px;top:92px;font-size:12.5px;line-height:16px">Veteran Business Owners<br>&amp; Portfolio Manager.</p>
      <p style="left:13px;top:146px;font:700 14px/25px 'Arimo',sans-serif">• Walter B. Hensley<br>• Daniel R. Pryce</p>
    </div>
    <svg class="arrow" style="left:220px" viewBox="0 0 36 16" aria-hidden="true"><rect x="0" y="5" width="24" height="6" fill="#1b76c9"/><polygon points="22,0 36,8 22,16" fill="#1b76c9"/></svg>

    <div class="ov-box dark" style="left:264px">
      <svg class="icon" style="left:22px;top:14px" width="30" height="30" viewBox="0 0 30 30" aria-hidden="true"><circle cx="15" cy="13" r="6" fill="#fff"/><rect x="12" y="19" width="6" height="5" fill="#fff"/><g stroke="#fff" stroke-width="2"><line x1="15" y1="1" x2="15" y2="4"/><line x1="4" y1="13" x2="7" y2="13"/><line x1="23" y1="13" x2="26" y2="13"/><line x1="7" y1="5" x2="9" y2="7"/><line x1="23" y1="5" x2="21" y2="7"/></g></svg>
      <h3 style="left:55px;top:22px;font-size:17px">STRATEGY</h3>
      <p style="left:16px;top:66px;width:155px">Bastion Meridian, LLC seeks to take advantage of any Price-Value mismatch or Supply-Demand imbalance throughout the economy; ranging from economic industries and sectors, down to an individual business, security, or commodity.</p>
    </div>
    <svg class="arrow" style="left:448px" viewBox="0 0 36 16" aria-hidden="true"><rect x="0" y="5" width="24" height="6" fill="#1b76c9"/><polygon points="22,0 36,8 22,16" fill="#1b76c9"/></svg>

    <div class="ov-box dark" style="left:489px">
      <svg class="icon" style="left:16px;top:14px" width="30" height="30" viewBox="0 0 30 30" aria-hidden="true"><circle cx="15" cy="15" r="12" fill="none" stroke="#fff" stroke-width="2.5"/><circle cx="15" cy="15" r="6" fill="none" stroke="#fff" stroke-width="2.5"/><line x1="15" y1="15" x2="27" y2="3" stroke="#fff" stroke-width="2.5"/></svg>
      <h3 style="left:52px;top:20px;font-size:15px">CORE FOCUS</h3>
      <p style="left:19px;top:60px;width:150px">Undervalued/Overvalued securities, contracts, or other instruments; Looking for opportunities to capture significant value where intensive and proprietary fundamental, technical, and psychological research aligns with both established principles and sound logic.</p>
    </div>
    <div class="page-num" style="left:663px;top:354px;background:#f6d7b5;color:#8a5a2a">3</div>
  </section>

  <!-- Why slide 1 -->
  <div class="accent-blue" style="left:547px;top:983px;width:190px;height:20px"></div>
  <div class="accent-blue" style="left:547px;top:1380px;width:190px;height:17px"></div>
  <section class="slide why" style="left:37px;top:992px;width:700px;height:396px" role="img" aria-label="Dim navy photo of a business team at work">
    <h2 style="left:31px;top:39px">WHY BASTION MERIDIAN?</h2>
    <div class="title-rule" style="left:31px;top:68px;width:198px"></div>

    <svg class="icon" style="left:33px;top:101px" width="22" height="22" viewBox="0 0 22 22" aria-hidden="true"><rect width="22" height="22" rx="2" fill="#fff"/><circle cx="11" cy="8" r="3" fill="#1f3a4c"/><circle cx="5.5" cy="9" r="2" fill="#1f3a4c"/><circle cx="16.5" cy="9" r="2" fill="#1f3a4c"/><path d="M3 17c1-5 15-5 16 0z" fill="#1f3a4c"/></svg>
    <div class="feat-head" style="left:62px;top:105px">EXPERIENCED TEAM</div>
    <div class="feat-text" style="left:72px;top:130px">Managing Members have more than 25 years combined experience across business management, financial markets, economics, research &amp; analytics.</div>

    <svg class="icon" style="left:43px;top:237px" width="24" height="24" viewBox="0 0 24 24" aria-hidden="true"><circle cx="12" cy="12" r="10" fill="none" stroke="#fff" stroke-width="2.2"/><circle cx="12" cy="12" r="5" fill="none" stroke="#fff" stroke-width="2.2"/><line x1="12" y1="12" x2="22" y2="2" stroke="#fff" stroke-width="2.2"/></svg>
    <div class="feat-head" style="left:71px;top:240px">DISCIPLINED PROCESS</div>
    <div class="feat-text serif-small" style="left:82px;top:263px;width:170px">We follow a disciplined process based on established principles and sound logic in accordance with the scientific method.</div>

    <div class="divider" style="left:260px;top:100px;height:210px"></div>

    <div class="abs serif" style="left:305px;top:84px;font-size:21px;line-height:26px;color:#fff">Methodical Application of<br>Knowledge and Experience</div>
    <div class="title-rule" style="left:302px;top:135px;width:240px;height:3px"></div>
    <div class="body" style="left:305px;top:155px;width:345px">Edmund Harlow and Julian Whitcombe respectively provide the description of our operating principles;</div>
    <ul class="body" style="left:305px;top:202px;width:345px">
      <li>Industry and Patience are the Surest Means to Plenty.”</li>
      <li>An Investment in Knowledge Always Pays the Best Interest.”</li>
      <li>Risk Comes from not Knowing What You are Doing.”</li>
      <li>Investment is most Intelligent when It’s most Business-Like.</li>
      <li>Know What You are Doing; Know Your Business.”</li>
    </ul>
    <div class="abs wordmark" style="left:46px;top:350px;font-size:15px;color:#fff">BASTION MERIDIAN LLC</div>
    <div class="page-num" style="left:684px;top:370px;background:#f6d7b5;color:#8a5a2a">4</div>
  </section>

  <!-- Why slide 2 -->
  <div class="accent-blue" style="left:1266px;top:977px;width:221px;height:20px"></div>
  <div class="accent-blue" style="left:1266px;top:1380px;width:221px;height:17px"></div>
  <div class="accent-blue" style="left:1475px;top:977px;width:12px;height:420px"></div>
  <section class="slide why" style="left:748px;top:987px;width:727px;height:401px" role="img" aria-label="Dim navy photo of a business team at work">
    <h2 style="left:31px;top:38px">WHY BASTION MERIDIAN? (CONTINUE)</h2>
    <div class="title-rule" style="left:31px;top:64px;width:168px"></div>

    <svg class="icon" style="left:34px;top:101px" width="22" height="22" viewBox="0 0 22 22" aria-hidden="true"><rect width="22" height="22" rx="2" fill="#fff"/><circle cx="11" cy="8" r="3" fill="#1f3a4c"/><circle cx="5.5" cy="9" r="2" fill="#1f3a4c"/><circle cx="16.5" cy="9" r="2" fill="#1f3a4c"/><path d="M3 17c1-5 15-5 16 0z" fill="#1f3a4c"/></svg>
    <div class="feat-head" style="left:63px;top:106px">EXPERIENCED TEAM</div>
    <div class="feat-text" style="left:73px;top:131px">Managing Members have more than 25 years combined experience across business management, financial markets, economics, research &amp; analytics.</div>

    <svg class="icon" style="left:44px;top:240px" width="24" height="24" viewBox="0 0 24 24" aria-hidden="true"><circle cx="12" cy="12" r="10" fill="none" stroke="#fff" stroke-width="2.2"/><circle cx="12" cy="12" r="5" fill="none" stroke="#fff" stroke-width="2.2"/><line x1="12" y1="12" x2="22" y2="2" stroke="#fff" stroke-width="2.2"/></svg>
    <div class="feat-head" style="left:72px;top:243px">DISCIPLINED PROCESS</div>
    <div class="feat-text serif-small" style="left:83px;top:266px;width:170px">We follow a disciplined process based on established principles and sound logic in accordance with the scientific method.</div>

    <div class="divider" style="left:264px;top:100px;height:210px"></div>

    <div class="abs serif" style="left:305px;top:84px;font-size:21px;font-weight:700;color:#fff;letter-spacing:.5px">CONSISTENT RESULTS</div>
    <div class="title-rule" style="left:305px;top:116px;width:172px;height:3px"></div>
    <div class="body" style="left:310px;top:156px;width:360px">Here again, Julian Whitcombe provides the clearest statement of our thinking…</div>
    <div class="body" style="left:310px;top:204px;width:360px">"An investment operation is one which upon thorough analysis offers safety of principal and a satisfactory return; Operations not meeting these requirements are speculative."</div>
    <div class="body" style="left:310px;top:284px;width:360px">Bastion Meridian, LLC is targeting the consistent safety of principal and a satisfactory annual return.</div>
    <div class="abs wordmark" style="left:46px;top:356px;font-size:15px;color:#fff">BASTION MERIDIAN LLC</div>
    <div class="page-num" style="left:702px;top:375px;background:#f6d7b5;color:#8a5a2a">5</div>
  </section>

</div>
</body>
</html>
```